Modern Yoga Studio Timetable and Flyer Design

We have a comprehensive class timetable and we are wanting to a clean modern look for our Spring timetable.

We require a double sided flyer with our class timetable included.
We would prefer an A5 size (postcard) or DL (1/3 A4).

We would like the final flyer to have.
Side A : Yoga image, logo

Cedar Pose Loft
address: 3/17 Weltmore Street, Parvindale
website: cedarpose.com.au
mobile: 0471 592 640

Side B: Clear easy to read timetable with a break down of class types and website.

We would also like to have a copy of the timetable itself as a separate jpg or pdf for use on our website to download.

Thank you.
Yours kindly,
Hilde

I have attached a sample of another timetable of which I like the look and feel of, however this is just a guide. I've also attached our 'new' schedule in WORD plus uploaded our last design of the front.

Target Market(s)

Women aged 30-45

Industry/Entity Type

Health And Wellness

Font styles to use
Other font styles liked:
• Brandon Grotesque, Jenna Sue

Colors
6c459b
33a6d7
ffffff

Requirements
Must have
• A definitive colour to decipher between different class types on our timetable. Where each colour represents a different class type. Colours and layouts similar to our website design, see www.cedarpose.com.au
Nice to have
• I've included a design of another studio whose timetable design I like. One of our own yoga images instead of a stock image.
Should not have
• No dark gridlines between the cells/boxes in the timetables. Please don't use stock yoga images.

```html
<!DOCTYPE html>
<html lang="en">
<head>
<meta charset="utf-8">
<title>Cedar Pose Loft – Spring Flyer</title>
<link href="https://fonts.googleapis.com/css2?family=Montserrat:wght@400;500;600;700&display=swap" rel="stylesheet">
<style>
  :root {
    --purple: #6c459b;
    --purple-deep: #3f1a55;
    --purple-ring: #4e2a72;
    --blue: #33a6d7;
    --white: #ffffff;
    --rise: #2f9e6e;
    --vinyasa: #33a6d7;
    --slow: #4cb660;
    --yin: #2f62a8;
    --pregnancy: #5a2f8e;
    --mumbaby: #b0609e;
    --kids: #d46d2a;
    --teens: #c5a03c;
    --restore: #e27b7a;
    --yinrestore: #3f86c8;
    --wellness: #a98bc0;
  }
  * { box-sizing: border-box; margin: 0; padding: 0; }
  html, body { width: 846px; height: 1200px; overflow: hidden; background: var(--white); }
  body { position: relative; font-family: "Montserrat", sans-serif; color: var(--white); }

  .flyer-side { position: absolute; left: 40px; width: 765px; overflow: hidden;
    box-shadow: 0 2px 6px rgba(0,0,0,.35); }
  .front { top: 40px; height: 539px; background: var(--white); }
  .back { top: 620px; height: 540px;
    background: linear-gradient(180deg, #3e8fc8 0%, #5a72b8 45%, #6a4aa0 100%); }

  .front-shapes { position: absolute; inset: 0; }
  .ornament-area { position: absolute; left: 20px; top: 10px; width: 360px; height: 140px;
    background: radial-gradient(ellipse at 50% 0%, rgba(108,69,155,.55), rgba(255,255,255,0) 70%); }
  .brand-top { position: absolute; left: 36px; top: 142px; font-size: 26px; font-weight: 400;
    letter-spacing: 6px; color: var(--blue); text-transform: lowercase; }
  .brand-bottom { position: absolute; right: 36px; top: 468px; font-size: 26px; font-weight: 400;
    letter-spacing: 5px; color: var(--white); text-transform: lowercase; }

  .studio-name { position: absolute; left: 36px; top: 296px; font-size: 22px; font-weight: 700;
    letter-spacing: 1px; text-transform: uppercase; }
  .contact-list { position: absolute; left: 32px; top: 342px; list-style: none; }
  .contact-list li { display: flex; align-items: center; height: 33.5px; font-size: 19px;
    font-weight: 500; letter-spacing: 1px; text-transform: uppercase; }
  .contact-list svg { width: 22px; height: 22px; margin-right: 14px; flex: none; }

  .timetable-title { position: absolute; left: 108px; top: 18px; font-size: 18px; font-weight: 600;
    letter-spacing: 1px; text-transform: uppercase; padding-bottom: 4px;
    border-bottom: 2px solid rgba(255,255,255,.8); }
  .photo-bg { position: absolute; left: 180px; top: 100px; width: 440px; height: 420px;
    background: radial-gradient(ellipse at 50% 50%, rgba(190,180,220,.35), rgba(255,255,255,0) 70%); }
  .day-row { position: absolute; left: 110.4px; top: 58px; display: grid;
    grid-template-columns: repeat(7, 87.2px); font-size: 13px; font-weight: 500; text-align: center; }
  .times { position: absolute; left: 0; top: 84.8px; width: 92px; list-style: none; }
  .times li { height: 31px; line-height: 31px; text-align: right; font-size: 11.5px; font-weight: 600; }
  .grid { position: absolute; left: 110.4px; top: 84.8px; width: 610.4px; display: grid;
    grid-template-columns: repeat(7, 87.2px); grid-template-rows: repeat(13, 31px); }
  .band { grid-column: 1 / 8; background: rgba(255,255,255,.2); }
  .band:nth-child(even) { background: rgba(255,255,255,.08); }
  .session { display: flex; align-items: center; justify-content: center; text-align: center;
    font-size: 10px; font-weight: 600; line-height: 1.15; text-transform: uppercase;
    box-shadow: inset 0 -2px 0 rgba(0,0,0,.15), 0 1px 2px rgba(0,0,0,.2); z-index: 1; }
  .rise { background: var(--rise); }
  .vinyasa { background: var(--vinyasa); }
  .slow { background: var(--slow); }
  .yin { background: var(--yin); }
  .pregnancy { background: var(--pregnancy); }
  .mumbaby { background: var(--mumbaby); }
  .kids { background: var(--kids); }
  .teens { background: var(--teens); }
  .restore { background: var(--restore); }
  .yinrestore { background: var(--yinrestore); }
  .wellness { background: var(--wellness); }
  .footnote { position: absolute; left: 108px; top: 505px; font-size: 11.5px; font-weight: 600;
    letter-spacing: .5px; text-transform: uppercase; }
  .web { position: absolute; right: 44px; top: 505px; font-size: 11.5px; font-weight: 600;
    letter-spacing: .5px; text-transform: uppercase; }
</style>
</head>
<body>

<section class="flyer-side front">
  <svg class="front-shapes" viewBox="0 0 765 539" width="765" height="539">
    <defs>
      <linearGradient id="front-purple" x1="0" y1="0" x2="0" y2="1">
        <stop offset="0" stop-color="#f4eff8"/>
        <stop offset=".35" stop-color="#8a63a8"/>
        <stop offset=".7" stop-color="#52236b"/>
        <stop offset="1" stop-color="#3f1a55"/>
      </linearGradient>
      <linearGradient id="photo-tone" x1="0" y1="0" x2="1" y2="1">
        <stop offset="0" stop-color="#d8eef9"/>
        <stop offset="1" stop-color="#3aa2d6"/>
      </linearGradient>
    </defs>
    <path d="M0 0 H560 V300 C520 380 420 470 300 500 C180 525 80 480 0 440 Z" fill="url(#front-purple)"/>
    <path d="M0 452 C120 510 260 520 400 470 C520 425 640 380 765 440 V539 H0 Z" fill="var(--blue)"/>
    <circle cx="568" cy="176" r="194" fill="var(--purple-ring)"/>
    <circle cx="568" cy="176" r="174" fill="url(#photo-tone)" role="img" aria-label="Yoga teacher in a side-angle pose on a mat, toned blue"/>
  </svg>
  <div class="ornament-area" role="img" aria-label="Decorative mandala pattern"></div>
  <div class="brand-top">cedar pose loft</div>

  <h1 class="studio-name">Cedar Pose Loft</h1>
  <ul class="contact-list">
    <li>
      <svg viewBox="0 0 24 24"><circle cx="12" cy="12" r="12" fill="#fff"/><path d="M12 5a4.5 4.5 0 0 0-4.5 4.5c0 3.4 4.5 8.5 4.5 8.5s4.5-5.1 4.5-8.5A4.5 4.5 0 0 0 12 5z" fill="#4a2060"/><circle cx="12" cy="9.5" r="1.7" fill="#fff"/></svg>
      3/17 Weltmore Street, Parvindale
    </li>
    <li>
      <svg viewBox="0 0 24 24"><circle cx="12" cy="12" r="11" fill="none" stroke="#fff" stroke-width="2"/><ellipse cx="12" cy="12" rx="4.5" ry="11" fill="none" stroke="#fff" stroke-width="1.6"/><path d="M1 12h22M3 7h18M3 17h18" stroke="#fff" stroke-width="1.6"/></svg>
      cedarpose.com.au
    </li>
    <li>
      <svg viewBox="0 0 24 24"><circle cx="12" cy="12" r="12" fill="#fff"/><path d="M8.2 6.5l2 2.3-1.1 1.6c.8 1.7 2 2.9 3.7 3.7l1.6-1.1 2.3 2-1.2 2c-4.6-.4-8.3-4.1-8.7-8.7z" fill="#4a2060"/></svg>
      0471 592 640
    </li>
  </ul>
  <div class="brand-bottom">cedar pose loft</div>
</section>

<section class="flyer-side back">
  <div class="photo-bg" role="img" aria-label="Faint photo of a yoga pose on a mat behind the timetable"></div>
  <h2 class="timetable-title">Cedar Pose Spring Timetable</h2>

  <div class="day-row"><span>MON</span><span>TUE</span><span>WED</span><span>THU</span><span>FRI</span><span>SAT</span><span>SUN</span></div>

  <ul class="times">
    <li>5.45 AM</li><li>9.00 AM</li><li>9.15 AM</li><li>9.30 AM</li><li>10.30 AM</li><li>11.00 AM</li>
    <li>12.15 PM</li><li>4.00 PM</li><li>4.45 PM</li><li>5.00 PM</li><li>6.00 PM</li><li>6.15 PM</li><li>7.30 PM</li>
  </ul>

  <div class="grid">
    <div class="band" style="grid-row:1"></div><div class="band" style="grid-row:2"></div>
    <div class="band" style="grid-row:3"></div><div class="band" style="grid-row:4"></div>
    <div class="band" style="grid-row:5"></div><div class="band" style="grid-row:6"></div>
    <div class="band" style="grid-row:7"></div><div class="band" style="grid-row:8"></div>
    <div class="band" style="grid-row:9"></div><div class="band" style="grid-row:10"></div>
    <div class="band" style="grid-row:11"></div><div class="band" style="grid-row:12"></div>
    <div class="band" style="grid-row:13"></div>

    <div class="session rise" style="grid-area:1/2">Rise &amp; Shine*</div>
    <div class="session rise" style="grid-area:1/4">Rise &amp; Shine*</div>
    <div class="session vinyasa" style="grid-area:2/6">Vinyasa<br>Flow</div>
    <div class="session vinyasa" style="grid-area:3/2">Vinyasa<br>Flow</div>
    <div class="session yin" style="grid-area:3/7">Yin</div>
    <div class="session slow" style="grid-area:4/1">Slow Flow</div>
    <div class="session vinyasa" style="grid-area:4/4">Vinyasa<br>Flow</div>
    <div class="session pregnancy" style="grid-area:5/6">Pregnancy*</div>
    <div class="session mumbaby" style="grid-area:6/2">Mum &amp; Baby*</div>
    <div class="session mumbaby" style="grid-area:6/4">Mum &amp; Baby*</div>
    <div class="session pregnancy" style="grid-area:7/4">Pregnancy*</div>
    <div class="session kids" style="grid-area:8/3">Kids 8-12*</div>
    <div class="session kids" style="grid-area:8/4">Kids 5-7*</div>
    <div class="session vinyasa" style="grid-area:8/6">Vinyasa<br>Flow</div>
    <div class="session teens" style="grid-area:9/3">Teens 12-16*</div>
    <div class="session teens" style="grid-area:10/4">Teens 12-16*</div>
    <div class="session pregnancy" style="grid-area:11/1">Pregnancy*</div>
    <div class="session vinyasa" style="grid-area:11/2">Vinyasa<br>Flow</div>
    <div class="session slow" style="grid-area:11/3">Slow Flow</div>
    <div class="session restore" style="grid-area:11/5">Flow &amp;<br>Restore</div>
    <div class="session pregnancy" style="grid-area:12/4">Pregnancy*</div>
    <div class="session vinyasa" style="grid-area:13/1">Vinyasa<br>Flow</div>
    <div class="session pregnancy" style="grid-area:13/2">Pregnancy*</div>
    <div class="session yinrestore" style="grid-area:13/3">Yin &amp;<br>Restore</div>
    <div class="session wellness" style="grid-area:13/4">Women's<br>Wellness</div>
  </div>

  <p class="footnote">* Bookings essential</p>
  <p class="web">www.cedarpose.com.au</p>
</section>

</body>
</html>
```